Clean and modern business cards

Looking for an updated business card design for my dental office “corvanta dental” . Looking for a modern clean / sleek design . I’m thinking black background but open to seeing other options . One side needs to have an appointment card . Card needs to have logo, dentist name , phone, email , address . I’ve attached couple of cards I thought were cool as well as my logo
Target Market(s)
Dental patients
Industry/Entity Type
Dentistry
Contact Information for Business Card
Phone email address

```html
<!DOCTYPE html>
<html lang="en">
<head>
<meta charset="utf-8">
<title>Corvanta Dental – Business & Appointment Card</title>
<link href="https://fonts.googleapis.com/css2?family=Montserrat:wght@400;500;600;700&display=swap" rel="stylesheet">
<style>
  :root {
    --backdrop: #3b3b3c;
    --card-black: #161616;
    --card-white: #ffffff;
    --lime: #8dc63f;
    --ink: #111111;
    --ink-soft: #2b2b2b;
    --rule-light: #6e6e6e;
    --icon-yellow: #f2c500;
    --icon-red: #e2452b;
    --icon-teal: #2bb3c8;
  }
  * { box-sizing: border-box; margin: 0; padding: 0; }
  html, body {
    width: 1200px; height: 801px; overflow: hidden;
    background: var(--backdrop);
    font-family: "Montserrat", sans-serif;
  }
  .sheet {
    width: 1200px; height: 801px;
    display: flex; align-items: center; justify-content: center; gap: 40px;
  }
  .card {
    position: relative;
    width: 520px; height: 297px;
    border-bottom: 4px solid var(--lime);
    box-shadow: 0 10px 24px rgba(0,0,0,.35);
  }

  /* Front: contact card */
  .card--contact { background: var(--card-black); color: #fff; }
  .wordmark {
    position: absolute; display: flex; align-items: center; gap: 10px;
    font-weight: 700; font-size: 22px; letter-spacing: .04em; text-transform: uppercase;
  }
  .wordmark__dot { width: 26px; height: 26px; border-radius: 50%; background: var(--lime); }
  .card--contact .wordmark { right: 34px; top: 38px; color: #fff; }
  .dentist-name {
    position: absolute; left: 34px; top: 146px;
    color: var(--lime); font-weight: 700; font-size: 20px;
  }
  .divider {
    position: absolute; left: 34px; right: 34px; top: 184px;
    height: 1px; background: var(--rule-light);
  }
  .contact-list {
    position: absolute; left: 34px; top: 200px; list-style: none;
    font-size: 13.5px; line-height: 21px; font-weight: 500;
  }
  .contact-list li { display: flex; align-items: center; gap: 9px; }
  .contact-list svg { width: 12px; height: 12px; flex: none; }
  .address {
    position: absolute; right: 34px; top: 200px; text-align: right;
    font-size: 13.5px; line-height: 21px; font-weight: 500;
  }

  /* Back: appointment card */
  .card--appointment { background: var(--card-white); color: var(--ink); }
  .card--appointment .wordmark { left: 150px; top: 30px; color: var(--ink); }
  .appointment-title {
    position: absolute; left: 0; right: 0; top: 92px; text-align: center;
    font-weight: 600; font-size: 15px; letter-spacing: .03em; text-transform: uppercase;
  }
  .field {
    position: absolute; left: 30px; right: 30px;
    display: flex; align-items: flex-end; gap: 4px;
    font-size: 15px; font-weight: 500;
  }
  .field__line { flex: 1; border-bottom: 1.5px dashed #555; margin-bottom: 4px; }
  .field--date { top: 134px; }
  .field--time { top: 170px; }
  .notice {
    position: absolute; right: 30px; top: 222px; width: 330px;
    font-size: 13.5px; line-height: 19px; color: var(--ink-soft); font-weight: 500;
  }
  .notice strong { color: var(--lime); font-weight: 700; }
</style>
</head>
<body>
<main class="sheet">
  <section class="card card--contact" aria-label="Business card front">
    <div class="wordmark"><span class="wordmark__dot"></span>Corvanta Dental</div>
    <p class="dentist-name">Dr. Lena Varsh</p>
    <div class="divider"></div>
    <ul class="contact-list">
      <li>
        <svg viewBox="0 0 12 12" aria-hidden="true"><path fill="var(--icon-yellow)" d="M2.5 1 4.5 1 5 3.6 3.8 4.6a6 6 0 0 0 3.6 3.6L8.4 7 11 7.5 11 9.5C11 10.3 10.3 11 9.5 11 5 11 1 7 1 2.5 1 1.7 1.7 1 2.5 1z"/></svg>
        (204)-555-0147
      </li>
      <li>
        <svg viewBox="0 0 12 12" aria-hidden="true"><rect x="0.5" y="2" width="11" height="8" rx="1" fill="var(--icon-red)"/><path d="M1 2.8 6 6.6 11 2.8" stroke="#161616" stroke-width="1.1" fill="none"/></svg>
        hello@corvantawpg.ca
      </li>
      <li>
        <svg viewBox="0 0 12 12" aria-hidden="true"><circle cx="6" cy="6" r="5.2" fill="none" stroke="var(--icon-teal)" stroke-width="1.4"/><path d="M1 6h10M6 1c-2.5 3-2.5 7 0 10M6 1c2.5 3 2.5 7 0 10" stroke="var(--icon-teal)" stroke-width="1" fill="none"/></svg>
        corvantawpg.ca
      </li>
    </ul>
    <p class="address">2480 Harrow Ave<br>Winnipeg, MB</p>
  </section>

  <section class="card card--appointment" aria-label="Appointment card">
    <div class="wordmark"><span class="wordmark__dot"></span>Corvanta Dental</div>
    <h2 class="appointment-title">Your next appointment is</h2>
    <div class="field field--date"><span>Date</span><span class="field__line"></span></div>
    <div class="field field--time"><span>Time</span><span class="field__line"></span><span>am/pm</span></div>
    <p class="notice">To cancel or reschedule please notify us at least <strong>48</strong> hours prior to your scheduled appointment</p>
  </section>
</main>
</body>
</html>
```